Specialised investor in e-mobility and energy wants business card design

We need a business card design that fits our existing corporate design. <The look and feel must be 'sharp'/'clean', dynamic, communicate momentum, professionalism etc (as one would imagine from a firm in the financial sector). We like the idea of a reverse-side of the card that includes the logo, and the name and contact details on the other. We expect the deliverable to be whatever format might be required to be able to get cards printed directly by a service such as tandor press. Our website is www.orm.capital

```html
<!DOCTYPE html>
<html lang="en">
<head>
<meta charset="utf-8">
<title>ORM Capital – Business Card</title>
<link href="https://fonts.googleapis.com/css2?family=Montserrat:wght@400;500;700&display=swap" rel="stylesheet">
<style>
  :root {
    --backdrop: #e8e4dd;
    --card-white: #ffffff;
    --brand-green: #2e4b22;
    --accent-green: #7ab342;
    --text-dark: #2b2b2b;
    --text-light: #ffffff;
  }
  * { margin: 0; padding: 0; box-sizing: border-box; }
  html, body {
    width: 900px; height: 1200px; overflow: hidden;
    background: var(--backdrop);
    font-family: "Montserrat", sans-serif;
  }
  .canvas { position: relative; width: 900px; height: 1200px; }
  .card {
    position: absolute; left: 80px; width: 742px; height: 441px;
    border-radius: 32px;
  }
  .card-front { top: 130px; background: var(--card-white); }
  .card-back { top: 638px; background: var(--brand-green); }

  .wordmark {
    position: absolute; display: flex; align-items: center; gap: 14px;
    font-weight: 500; letter-spacing: 0.5px; white-space: nowrap;
  }
  .wordmark .dot { border-radius: 50%; background: var(--accent-green); }
  .card-front .wordmark { left: 28px; top: 70px; font-size: 58px; color: var(--brand-green); }
  .card-front .wordmark .dot { width: 22px; height: 22px; }
  .card-back .wordmark {
    left: 0; right: 0; top: 180px; justify-content: center;
    font-size: 74px; color: var(--text-light);
  }
  .card-back .wordmark .dot { width: 28px; height: 28px; }

  .person-name {
    position: absolute; left: 37px; top: 270px;
    font-size: 26px; font-weight: 700; color: var(--brand-green);
  }
  .person-role {
    position: absolute; left: 38px; top: 302px;
    font-size: 16px; color: var(--text-dark);
  }
  .divider {
    position: absolute; left: 38px; top: 333px; width: 668px; height: 2px;
    background: var(--accent-green);
  }
  .contact-list {
    position: absolute; left: 37px; top: 354px; list-style: none;
    font-size: 16px; color: var(--text-dark); line-height: 22.5px;
  }
  .contact-list li { display: flex; align-items: center; gap: 12px; }
  .contact-list svg { width: 14px; height: 14px; fill: var(--accent-green); }
  .address {
    position: absolute; left: 470px; top: 379px;
    font-size: 16px; color: var(--text-dark); line-height: 20px; font-style: normal;
  }
</style>
</head>
<body>
<div class="canvas">
  <section class="card card-front">
    <div class="wordmark"><span class="dot"></span>ORM Capital</div>
    <h1 class="person-name">Dale Marwick</h1>
    <p class="person-role">Owner</p>
    <div class="divider"></div>
    <ul class="contact-list">
      <li><svg viewBox="0 0 16 16" aria-hidden="true"><path d="M2 5c0-2 3-3 6-3s6 1 6 3v1h-3V5H5v1H2z M4 7h8l2 6H2z"/></svg>+41 70418 2296</li>
      <li><svg viewBox="0 0 16 16" aria-hidden="true"><path d="M1 3h14v10H1z M1 3l7 6 7-6" stroke="#fff" stroke-width="1.2"/></svg>dale@orm.capital</li>
      <li><svg viewBox="0 0 16 16" aria-hidden="true"><circle cx="8" cy="8" r="7"/><path d="M1 8h14M8 1c-3 3-3 11 0 14M8 1c3 3 3 11 0 14" stroke="#fff" stroke-width="1" fill="none"/></svg>www.orm.capital.com</li>
    </ul>
    <address class="address">48 Meridian Way, Suite 210<br>Alden, PA 19036</address>
  </section>

  <section class="card card-back">
    <div class="wordmark"><span class="dot"></span>ORM Capital</div>
  </section>
</div>
</body>
</html>
```